依頼概要
■ 重視する点/検討基準
添付させて頂いてますロゴを使った、名刺のデザインをお願いします。
大手企業の名刺のように、あまりごちゃごちゃせずに堅い印象を出して欲しいですが、ご自由にデザインして下さい。

2つの会社名を入れて下さい。
株式会社 フォルテア (工事・保守サービス部)
株式会社 NV・QUARTEL

通信事業部 役職
名前
アルファベット読み仮名

住所
電話番号
FAX番号
ADRESS  住所等は1つです。

㈱フォルテアがメインの会社ですので、社名フォルテアのみのバージョンもお願いします。

名刺最下部に5ミリ位のラインが入っている感じか、どこかにラインが入った感じが好きです。

横書きのみ。
紙の色は、真っ白または、少しだけクリームっぽい白(再生紙系)
2色か3色カラー

好きな色・・・赤・グレー

■ 利用用途
名刺

■ その他/注意点 ロゴはあまり大きくせず普通サイズにして下さい。
添付しているロゴは字体が2種類あるとので、各一つずつご提案下さい。
大文字、小文字のバージョンはどちらでも良いです。
画像はグラデーションになっているものですが、今回は名刺なのでベタの物を使います。
フォルテアのみというのは単純に、社名の所だけ、㈱NV・QUARTELを消して頂き、デザイン等はそのままで良いです。

以上宜しくお願いします。
宜しくお願いします。
宜しくお願いします。
FORTEAの文字が下に付いているロゴのバージョンで、デザインをお願いします。
添付データ 21番、25番、55番 どのロゴを使うか悩んでいますので、自由にご提案下さい。

宜しくお願いします。
フォルテアのみのデザインの場合、右側(工事・保守サービス部)は無しにして下さい。

住所、電話番号は下の方で、それ以外はご自由にデザインして下さい。
■ 選んだ理由

名刺でラインが真ん中に入っている等、ありそうでなかなかないデザインでシンプルで、派手すぎずクールなイメージが良かったです。

■ 提案者全員へのお礼・コメント

沢山の参考になるご提案ありがとうございました。
また修正も迅速に対応して頂き有難うございました。

```html
<!DOCTYPE html>
<html lang="ja">
<head>
<meta charset="utf-8">
<title>名刺デザイン案 フォルテア</title>
<link rel="stylesheet" href="https://fonts.googleapis.com/css2?family=Noto+Sans+JP:wght@400;500&family=Noto+Serif+JP:wght@400;600;700&display=swap">
<style>
  :root{
    --paper:#ffffff;
    --ink:#1a1a1a;
    --red:#e2141f;
    --grey:#c9c9c9;
    --frame:#9a9a9a;
  }
  html,body{margin:0;padding:0;overflow:hidden;background:var(--paper);}
  .sheet{position:relative;width:758px;height:1200px;background:var(--paper);color:var(--ink);font-family:"Noto Serif JP",serif;}
  .plan-label{position:absolute;left:0;width:758px;text-align:center;font-family:"Noto Sans JP",sans-serif;font-size:28px;font-weight:400;}
  .card{position:absolute;left:13px;width:732px;border:1.5px solid var(--frame);background:var(--paper);box-sizing:border-box;}
  .card-a{top:56px;height:464px;}
  .card-b{top:752px;height:438px;}
  .brand{position:absolute;left:22px;top:16px;width:140px;text-align:center;}
  .brand-dot{display:block;width:104px;height:104px;border-radius:50%;background:var(--red);margin:0 auto 6px;}
  .brand-name{font-family:"Noto Serif JP",serif;font-weight:700;font-size:28px;color:var(--red);letter-spacing:1px;line-height:1;}
  .accent-line{position:absolute;left:0;width:732px;height:14px;}
  .card-a .accent-line{top:190px;}
  .card-b .accent-line{top:136px;}
  .company{position:absolute;font-weight:600;white-space:nowrap;line-height:1;}
  .company small{font-size:17px;font-weight:600;}
  .card-a .company-main{left:198px;top:34px;font-size:25px;}
  .card-a .company-sub{left:198px;top:77px;font-size:25px;}
  .card-b .company-main{left:258px;top:62px;font-size:27px;}
  .role{position:absolute;font-size:17px;font-weight:600;}
  .person{position:absolute;font-size:38px;font-weight:700;letter-spacing:6px;line-height:1;}
  .romaji{position:absolute;font-size:18px;letter-spacing:1px;}
  .card-a .role{left:318px;top:222px;}
  .card-a .person{left:420px;top:215px;}
  .card-a .romaji{left:424px;top:262px;}
  .card-b .role{left:262px;top:226px;}
  .card-b .person{left:432px;top:219px;}
  .card-b .romaji{left:436px;top:265px;}
  .contact{position:absolute;left:12px;margin:0;font-size:17px;line-height:30px;white-space:pre;}
  .card-a .contact{top:330px;}
  .card-b .contact{top:338px;}
</style>
</head>
<body>
<main class="sheet">
  <svg width="0" height="0" style="position:absolute">
    <defs>
      <linearGradient id="accentFade" x1="0" x2="1" y1="0" y2="0">
        <stop offset="0" stop-color="#e2141f"/>
        <stop offset="0.55" stop-color="#e2141f"/>
        <stop offset="1" stop-color="#d6d6d6"/>
      </linearGradient>
    </defs>
  </svg>

  <div class="plan-label" style="top:4px;">No.9</div>
  <section class="card card-a">
    <div class="brand"><span class="brand-dot"></span><span class="brand-name">FORTEA</span></div>
    <div class="company company-main">株式会社 フォルテア<small>（工事・保守サービス部）</small></div>
    <div class="company company-sub">株式会社 NV・QUARTEL</div>
    <svg class="accent-line" viewBox="0 0 732 14" preserveAspectRatio="none">
      <polygon points="168,2 732,6 732,10 168,12" fill="url(#accentFade)"/>
    </svg>
    <div class="role">役職</div>
    <div class="person">佐藤 健二</div>
    <div class="romaji">Sato Kenji</div>
    <p class="contact">〒000-1234　□□県□□市□□町□□-□□
TEL　012-456-7890　/　FAX　012-456-7891
Mail　address_00@fortea.com</p>
  </section>

  <div class="plan-label" style="top:698px;">No.12</div>
  <section class="card card-b">
    <div class="brand"><span class="brand-dot"></span><span class="brand-name">FORTEA</span></div>
    <div class="company company-main">株式会社 フォルテア</div>
    <svg class="accent-line" viewBox="0 0 732 14" preserveAspectRatio="none">
      <polygon points="180,2 732,6 732,10 180,12" fill="url(#accentFade)"/>
    </svg>
    <div class="role">役職</div>
    <div class="person">佐藤 健二</div>
    <div class="romaji">Sato Kenji</div>
    <p class="contact">〒000-1234　□□県□□市□□町□□-□□
TEL　012-456-7890　/　FAX　012-456-7891
Mail　address_00@fortea.com</p>
  </section>
</main>
</body>
</html>
```